Dynamic Business Card for Sports Supplements Company

Hi! I'm looking for an awesome business card to match my existing sports supplement company. I have uploaded my current company logo and screenshot of the front page of my website.

I would like to have something dynamic and interesting and utilize the colors in the website - the reds and purples

The business card should be double sided and focus on a unique eye-catching design on the back and include all the relevant company info.

Most importantly, it should say somewhere: "Sign up on our website for a coupon code."

Target Market(s)

Mostly for women gym goers but it shouldn't be too feminine. It should be in keeping with the website design. It should flow and clearly be connected to it

Industry/Entity Type

Business

Contact Information for Business Card

Lorena K. Vasquez
CEO
LVasquez@Fortivanco.example
www.fortivanco.example
614.275.3081
P.O. Box 48317
Corvale, Oregon 22417

Sign up on our website for a coupon code

Font styles to use
Serif
Sans Serif
Other font styles liked:
• Novecento font family and "Fortivan" is in AR Destine font

Requirements
Must have
• One side should be a bold Fortivan logo design. Even just the symbol itself may be o.k. (see attached file)

```html
<!DOCTYPE html>
<html lang="en">
<head>
<meta charset="utf-8">
<title>Fortivan Business Card</title>
<link rel="stylesheet" href="https://fonts.googleapis.com/css2?family=Aldrich&display=swap">
<style>
  :root {
    --ink: #231f20;
    --accent: #ed1c24;
    --paper: #ffffff;
    --frame: #000000;
  }
  html, body {
    margin: 0;
    padding: 0;
    width: 1200px;
    height: 686px;
    overflow: hidden;
    background: var(--paper);
  }
  .card {
    position: relative;
    width: 1200px;
    height: 686px;
    box-sizing: border-box;
    border: 4px solid var(--frame);
    background: var(--paper);
    font-family: "Aldrich", sans-serif;
    color: var(--ink);
  }
  .brand {
    position: absolute;
    left: 44px;
    top: 240px;
    display: flex;
    align-items: center;
    gap: 18px;
  }
  .brand-mark {
    width: 52px;
    height: 52px;
    background: var(--accent);
  }
  .brand-name {
    font-size: 68px;
    line-height: 1;
    letter-spacing: 2px;
    color: var(--ink);
    text-transform: uppercase;
  }
  .promo {
    position: absolute;
    left: 576px;
    top: 88px;
    margin: 0;
    font-size: 44px;
    line-height: 58px;
    letter-spacing: 3px;
    font-weight: 400;
    color: var(--accent);
  }
  .contact-person {
    position: absolute;
    left: 42px;
    top: 414px;
    margin: 0;
  }
  .person-name {
    display: block;
    font-size: 47px;
    line-height: 52px;
    letter-spacing: 2px;
  }
  .person-line {
    display: block;
    font-size: 34px;
    line-height: 46px;
    letter-spacing: 1px;
  }
  .person-line.web {
    color: var(--accent);
  }
  .contact-office {
    position: absolute;
    left: 870px;
    top: 412px;
    margin: 0;
    font-style: normal;
    font-size: 34px;
    line-height: 46px;
    letter-spacing: 1.5px;
  }
  .contact-office span {
    display: block;
  }
</style>
</head>
<body>
  <main class="card">
    <div class="brand">
      <div class="brand-mark" aria-hidden="true"></div>
      <div class="brand-name">Fortivan</div>
    </div>

    <p class="promo">Sign up on our website<br>for a coupon code!</p>

    <div class="contact-person">
      <span class="person-name">Lorena K. Vasquez</span>
      <span class="person-line">CEO</span>
      <span class="person-line">LVasquez@Fortivanco.example</span>
      <span class="person-line web">www.fortivanco.example</span>
    </div>

    <address class="contact-office">
      <span>614.275.3081</span>
      <span>P.O. Box 48317</span>
      <span>Corvale, Oregon</span>
      <span>22417</span>
    </address>
  </main>
</body>
</html>
```